Corvell Tarn manufacturing Project

We are looking at getting a brand new design for a new company that deals in selling stainless tubing and other stainless still products such as handrails, Spigots, Balustrade Fittings
Glass, Glass fittings and Aluminium Channels

We require a very clean website that deals with the following colours:

Blue to light blues
Blacks
Greys to light Greys
Whites

We are open for other ideas BUT we *DO NOT* want any pinks, greens or bright colours except for backgrounds colours we have chosen above. (It can be solid, gradient or a subtle pattern)

YOU MUST KEEP THE LOGO AS IS. PLEASE DO NOT ALTER THE LOGO IN *ANY WAY* and the logo MUST be the same colours and fonts.

Logo is attached.

The site must contain these aspects:
jQuery Slider (Image slide show)
Top drop down Menus
Be no more than 900px wide
Text is to be to the k9R standards. (no special fonts)

We will chop up the design into html format. You just need to provide the PSD file.

The clients opposition is:
www.polbrenwick.com

It Company

• Alter the logo in anyway

```html
<!DOCTYPE html>
<html lang="en">
<head>
<meta charset="utf-8">
<title>Corvell Tarn Metal</title>
<link rel="stylesheet" href="https://fonts.googleapis.com/css2?family=Gelasio:wght@400;700&family=Arimo:wght@400;700&display=swap">
<style>
:root{
  --page:#f1f1f1;
  --page-light:#fafafa;
  --band:#1e1e1e;
  --band-light:#2c2c2c;
  --ink:#1a1a1a;
  --body:#444;
  --muted:#8a8a8a;
  --blue:#2f6fa6;
  --blue-dark:#1f4f80;
  --blue-light:#5a93c6;
  --line:#d8d8d8;
  --field:#fafafa;
  --photo:#d4d4d4;
  --photo-light:#efefef;
}
*{box-sizing:border-box;margin:0;padding:0}
html,body{width:883px;height:1200px;overflow:hidden}
body{font-family:"Arimo",Arial,sans-serif;color:var(--body);
  background:linear-gradient(135deg,var(--page-light),var(--page) 60%,var(--page-light));position:relative}
.serif{font-family:"Gelasio",Georgia,serif}
.abs{position:absolute}

/* header */
.brand{left:185px;top:6px;width:100px;text-align:center}
.brand-mark{width:44px;height:44px;border-radius:50%;background:var(--band);margin:0 auto 3px}
.brand-name{font-family:"Gelasio",Georgia,serif;font-size:11px;font-weight:700;color:var(--ink);white-space:nowrap}
.brand-sub{font-size:5px;color:var(--muted);letter-spacing:.5px}
.nav{left:413px;top:14px;display:flex;gap:20px}
.nav a{text-decoration:none;font-family:"Gelasio",Georgia,serif;font-size:10px;font-weight:700;color:var(--ink);display:block;line-height:1}
.nav small{display:block;font-family:"Arimo",Arial,sans-serif;font-weight:400;font-size:6px;color:var(--muted);margin-top:3px}
.search{left:415px;top:45px;width:286px;height:29px;border:1px solid var(--line);background:#fff;
  font-size:9px;color:#aaa;padding:9px 8px}
.search svg{position:absolute;right:8px;top:7px}

/* slider band */
.band{left:0;top:80px;width:883px;height:203px;background:linear-gradient(135deg,var(--band-light),var(--band))}
.slide{left:183px;top:93px;width:517px;height:207px;border-radius:4px;
  background:linear-gradient(160deg,#f4f4f4 0%,#c9c9c9 45%,#8e8e8e 75%,#e8e8e8 100%)}
.dots{left:194px;top:282px;display:flex;gap:3px}
.dots i{width:8px;height:8px;border-radius:50%;background:#333;border:1px solid #888}

.headline{left:0;top:310px;width:883px;text-align:center;font-size:16px;font-weight:700;color:var(--ink)}
.rule{height:1px;background:var(--line)}

/* products */
.product{width:162px}
.product h3{font-family:"Gelasio",Georgia,serif;font-weight:400;font-size:12.5px;color:var(--blue);line-height:1}
.product .tag{font-size:6.5px;color:var(--muted);margin-top:2px}
.product .shot{margin-top:8px;height:113px;border:1px solid #e2e2e2;
  background:radial-gradient(circle at 50% 50%,var(--photo-light),var(--photo))}
.product p{font-size:7.8px;line-height:1.35;margin-top:12px;height:54px;color:var(--body)}
.btn{display:flex;justify-content:space-between;align-items:center;height:19px;padding:0 7px;
  font-size:7px;text-decoration:none;border-radius:2px}
.btn-grey{width:89px;color:var(--blue);background:linear-gradient(#f6f6f6,#dcdcdc);border:1px solid #ccc;margin-top:12px}
.btn-blue{width:93px;color:#fff;background:linear-gradient(var(--blue-light),var(--blue-dark));border:1px solid var(--blue-dark)}

/* lower */
.col h4{font-family:"Gelasio",Georgia,serif;font-weight:400;font-size:11px;color:var(--ink);
  padding-bottom:6px;border-bottom:1px solid var(--line)}
.col p{font-size:7.5px;line-height:1.5;color:var(--ink)}
.field{border:1px solid var(--line);background:var(--field);font-size:6px;color:#bbb;padding:5px 6px;height:20px;margin-top:8px}
.dl{display:flex;gap:6px;padding-bottom:6px;border-bottom:1px solid var(--line);margin-top:6px}
.dl .thumb{width:27px;height:30px;flex:none;background:linear-gradient(135deg,#bdbdbd,#6f7a80)}
.dl p{font-size:6.5px;line-height:1.3;color:var(--blue-dark)}
.social{display:flex;gap:10px;margin-top:6px}
.social span{width:31px;height:31px;border-radius:4px;background:var(--blue)}

.footer{left:0;top:1143px;width:883px;height:57px;background:var(--band);color:#bbb;font-size:6.3px;line-height:1.9}
</style>
</head>
<body>

<header>
  <div class="brand abs">
    <div class="brand-mark"></div>
    <div class="brand-name">Corvell Tarn Metal</div>
    <div class="brand-sub">Manufacturing Co.,Ltd.</div>
  </div>
  <nav class="nav abs">
    <a href="#">HOME<small>Back to home</small></a>
    <a href="#">PRODUCTS<small>What we have for you</small></a>
    <a href="#">ABOUT US<small>Who we are</small></a>
    <a href="#">DOWNLOAD<small>Grab it</small></a>
    <a href="#">CONTACT<small>How to reach us</small></a>
  </nav>
  <div class="search abs">Search Products...
    <svg width="12" height="13" viewBox="0 0 12 13"><circle cx="5" cy="5" r="4" fill="none" stroke="#999" stroke-width="2"/><path d="M8 8l3 4" stroke="#999" stroke-width="2.4"/></svg>
  </div>
</header>

<div class="band abs"></div>
<div class="slide abs" role="img" aria-label="Brushed stainless steel handrail bending into a round wall flange"></div>
<div class="dots abs"><i></i><i></i><i></i><i></i><i></i></div>

<h1 class="headline abs serif">Lorem ipsum dolor sit amet, consectetur adipisicing elit</h1>
<div class="rule abs" style="left:183px;top:337px;width:517px"></div>

<section class="product abs" style="left:183px;top:358px">
  <h3>RailingSystem</h3><div class="tag">All you want your website to do</div>
  <div class="shot" role="img" aria-label="Polished stainless elbow fitting"></div>
  <p>Sed ut perspiciatis unde omnis iste natus error sit voluptatem accusantium doloremque laudantium, totam rem aperiam, eaque ipsa quae ab illo inventore veritatis et quasi architecto beatae vitae dicta sunt</p>
  <a class="btn btn-grey" href="#">View More<span>→</span></a>
</section>
<section class="product abs" style="left:360px;top:358px">
  <h3>Glass System</h3><div class="tag">A tool anything and everything you can think</div>
  <div class="shot" role="img" aria-label="Stainless tube base flange"></div>
  <p>Nemo enim ipsam voluptatem quia voluptas sit aspernatur aut odit aut fugit, sed quia consequuntur magni dolores eos qui ratione voluptatem sequi nesciunt tdolore magnam aliquam quaerat voluptatem.</p>
  <a class="btn btn-grey" href="#">View More<span>→</span></a>
</section>
<section class="product abs" style="left:538px;top:358px">
  <h3>Post &amp; Balustrade</h3><div class="tag">Fresh, Modern and ready for future</div>
  <div class="shot" role="img" aria-label="Stainless glass clamp"></div>
  <p>Neque porro quisquam est, qui dolorem ipsum quia dolor sit amet, consectetur, adipisci velit, sed quia non numquam eius modi tempora incidunt ut labore et dolore magnam aliquam quaerat voluptatem.</p>
  <a class="btn btn-grey" href="#">View More<span>→</span></a>
</section>

<section class="product abs" style="left:183px;top:636px">
  <h3>Accessories</h3><div class="tag">All you want your website to do</div>
  <div class="shot" role="img" aria-label="Polished stainless elbow fitting"></div>
  <p>Sed ut perspiciatis unde omnis iste natus error sit voluptatem accusantium doloremque laudantium, totam rem aperiam, eaque ipsa quae ab illo inventore veritatis et quasi architecto beatae vitae dicta sunt</p>
  <a class="btn btn-grey" href="#">View More<span>→</span></a>
</section>
<section class="product abs" style="left:360px;top:636px">
  <h3>Square tube Fittings</h3><div class="tag">A tool anything and everything you can think</div>
  <div class="shot" role="img" aria-label="Stainless tube base flange"></div>
  <p>Nemo enim ipsam voluptatem quia voluptas sit aspernatur aut odit aut fugit, sed quia consequuntur magni dolores eos qui ratione voluptatem sequi nesciunt tdolore magnam aliquam quaerat voluptatem.</p>
  <a class="btn btn-grey" href="#">View More<span>→</span></a>
</section>
<section class="product abs" style="left:538px;top:636px">
  <h3>Sliding door &amp; Canopy</h3><div class="tag">Fresh, Modern and ready for future</div>
  <div class="shot" role="img" aria-label="Stainless glass clamp"></div>
  <p>Neque porro quisquam est, qui dolorem ipsum quia dolor sit amet, consectetur, adipisci velit, sed quia non numquam eius modi tempora incidunt ut labore et dolore magnam aliquam quaerat voluptatem.</p>
  <a class="btn btn-grey" href="#">View More<span>→</span></a>
</section>

<div class="rule abs" style="left:183px;top:911px;width:517px"></div>

<section class="col abs" style="left:185px;top:936px;width:162px">
  <h4>Welcome</h4>
  <p style="margin-top:8px">Corvell Tarn Metal is always innovating to satisfy our customers by supplying solution of customer's inquiry, supply a modular Railing system which is easy to use and competitively priced, develop...</p>
  <a class="btn btn-blue" href="#" style="margin-top:6px">View More<span>→</span></a>
  <h4 style="margin-top:18px">Social Connection</h4>
  <p style="margin-top:6px;font-size:6.5px;line-height:1.3">At vero eos et accusamus et iusto odio dignissimos ducimus qui blanditiis praesentium</p>
  <div class="social"><span></span><span></span><span></span></div>
</section>

<section class="col abs" style="left:360px;top:936px;width:162px">
  <h4>Contact</h4>
  <div class="field">Your name</div>
  <div class="field">Your email address</div>
  <div class="field" style="height:80px">message</div>
  <a class="btn btn-blue" href="#" style="margin-top:6px;width:90px">Send it<span>→</span></a>
</section>

<section class="col abs" style="left:535px;top:936px;width:165px">
  <h4>Download</h4>
  <div class="dl"><div class="thumb" role="img" aria-label="Railing product photo"></div><p>Lorem ipsum dolor sit amet, consectetur adipisicing elit, sed do eiusmod tempor incididunt ut labore et dolore magna aliqua</p></div>
  <div class="dl"><div class="thumb" role="img" aria-label="Fitting product photo"></div><p>Sed ut perspiciatis unde omnis iste natus error sit voluptatem accusantium doloremque laudantium, totam rem aperiam.</p></div>
  <div class="dl"><div class="thumb" role="img" aria-label="Tube product photo"></div><p>At vero eos et accusamus et iusto odio dignissimos ducimus qui blanditiis praesentium.</p></div>
  <a class="btn btn-blue" href="#" style="margin-top:8px;width:90px">View All<span>→</span></a>
</section>

<footer class="footer abs">
  <div class="abs" style="left:186px;top:13px">Design and Developed by Harborline Studio<br>Home | About | Products | Download | Contact<br>Privacy Policy | Terms of use</div>
  <div class="abs" style="left:535px;top:13px">Copyright 2013, Harborline Studio. All Rights Reserved.</div>
</footer>

</body>
</html>
```